New business card for civil engineering company - "Keystone Audit"

We need a business card designed for our new structural engineering company.

The company name is "Keystone Audit" logo files attached.

We would like the following:
* Two-sided card
* Simple design

Information to be placed on the card:
Name - Marcus Dellow
Job Title - Director / Structural Engineer
Credentials - BEng(Hons), CPEng, CMengNZ, IntPE(NZ)
Email - marcus.dellow@keystoneaudit.co.nz
mobile - 0219364058
website - www.keystoneaudit.co.nz

```html
<!DOCTYPE html>
<html lang="en">
<head>
<meta charset="utf-8">
<title>Keystone Audit — Business Card</title>
<link href="https://fonts.googleapis.com/css2?family=Lato:ital,wght@0,400;0,700;1,400&display=swap" rel="stylesheet">
<style>
  :root {
    --backdrop: #b9b9b9;
    --card-white: #ffffff;
    --card-dark: #38383a;
    --brand-blue: #2a7fc6;
    --brand-blue-light: #8fcaea;
    --text-dark: #2f2f2f;
    --text-light: #ffffff;
  }
  html, body {
    margin: 0;
    padding: 0;
    width: 1200px;
    height: 802px;
    overflow: hidden;
    background: var(--backdrop);
    font-family: "Lato", Arial, sans-serif;
  }
  .canvas {
    position: relative;
    width: 1200px;
    height: 802px;
  }
  .card {
    position: absolute;
    top: 274px;
    width: 442px;
    height: 265px;
    box-shadow: 0 3px 6px rgba(0,0,0,0.35);
    overflow: hidden;
  }
  /* Front */
  .card--front {
    left: 136px;
    background: var(--card-white);
  }
  .front__band {
    position: absolute;
    left: 0; top: 0;
    width: 39px; height: 100%;
    background: var(--card-dark);
  }
  .front__rule {
    position: absolute;
    left: 42px; top: 0;
    width: 4px; height: 100%;
    background: var(--brand-blue);
  }
  .front__brand {
    position: absolute;
    right: 40px;
    top: 40px;
    display: flex;
    align-items: center;
    gap: 9px;
  }
  .brand__mark {
    width: 30px;
    height: 30px;
    background: var(--brand-blue);
  }
  .brand__name {
    font-weight: 700;
    font-size: 21px;
    letter-spacing: 1px;
    color: var(--text-dark);
  }
  .person {
    position: absolute;
    left: 67px;
    top: 124px;
  }
  .person__name {
    margin: 0;
    font-weight: 700;
    font-size: 17px;
    color: var(--brand-blue);
    letter-spacing: 0.3px;
    line-height: 1.1;
  }
  .person__role {
    margin: 1px 0 0;
    font-size: 13px;
    color: var(--text-dark);
  }
  .person__credentials {
    margin: 3px 0 0;
    font-size: 13px;
    font-style: italic;
    color: var(--text-dark);
  }
  .contacts {
    position: absolute;
    left: 67px;
    top: 195px;
    margin: 0;
    padding: 0;
    list-style: none;
  }
  .contacts li {
    display: flex;
    align-items: center;
    gap: 4px;
    height: 16px;
    font-size: 12.5px;
    color: var(--text-dark);
  }
  .contacts svg {
    width: 10px;
    height: 10px;
    fill: var(--brand-blue);
    flex: none;
  }
  /* Back */
  .card--back {
    left: 624px;
    background: var(--card-dark);
  }
  .back__brand {
    position: absolute;
    left: 0; right: 0;
    top: 80px;
    display: flex;
    flex-direction: column;
    align-items: center;
    gap: 22px;
  }
  .back__brand .brand__mark {
    width: 64px;
    height: 64px;
  }
  .back__brand .brand__name {
    font-size: 23px;
    color: var(--text-light);
  }
</style>
</head>
<body>
<main class="canvas">
  <section class="card card--front" aria-label="Business card front">
    <div class="front__band"></div>
    <div class="front__rule"></div>
    <div class="front__brand">
      <span class="brand__mark"></span>
      <span class="brand__name">KEYSTONE AUDIT</span>
    </div>
    <div class="person">
      <h1 class="person__name">MARCUS DELLOW</h1>
      <p class="person__role">Director / Structural Engineer</p>
      <p class="person__credentials">BEng(Hons), CPEng, CMengNZ, IntPE(NZ)</p>
    </div>
    <ul class="contacts">
      <li>
        <svg viewBox="0 0 10 10" aria-hidden="true"><path d="M2.5 0h5a1 1 0 0 1 1 1v8a1 1 0 0 1-1 1h-5a1 1 0 0 1-1-1V1a1 1 0 0 1 1-1zm.5 1.2v6.6h4V1.2zm2 7.1a.6.6 0 1 0 0 1.2.6.6 0 0 0 0-1.2z"/></svg>
        0219364058
      </li>
      <li>
        <svg viewBox="0 0 10 10" aria-hidden="true"><path d="M0 2h10v6H0zm1 .8v.3l4 2.6 4-2.6v-.3zm0 1.3V7.2h8V4.1L5 6.7z"/></svg>
        marcus.dellow@keystoneaudit.co.nz
      </li>
      <li>
        <svg viewBox="0 0 10 10" aria-hidden="true"><circle cx="5" cy="5" r="5"/></svg>
        www.keystoneaudit.co.nz
      </li>
    </ul>
  </section>

  <section class="card card--back" aria-label="Business card back">
    <div class="back__brand">
      <span class="brand__mark"></span>
      <span class="brand__name">KEYSTONE AUDIT</span>
    </div>
  </section>
</main>
</body>
</html>
```